BrightLane Real Estate Sign

We are in the process of rebranding our business and need a new For Sale \ Sold sign.
We're a prestige real estate agency and therefore require a really stylish sign.
I've uploaded the following files
1. The new company logo
2. "sample sign.jpg" which shows the type of sign we would like. It is a metal sign with a top panel and bottom panel.
3. Our previous sign "previous sign.jpg" if you're interested in seeing it.
The sign must be black with white text.
Our thoughts are that the top panel (refer to sample sign) would contain the text "For Sale" or "Sold". These would be two separate panels which are interchangeable and could be screwed in place.
The bottom panel would not contain any photos like the sample. However, it may contain our logo and my contact details etc.
The sign is 900mm wide x 1200mm high.
My details are:
Name: Desmond Harlow
Web: www.blrealestate.com.au
Email: sales@blrealestate.com.au
Phone: 0491 836 205

```html
<!DOCTYPE html>
<html lang="en">
<head>
<meta charset="UTF-8">
<title>BrightLane Real Estate – For Sale Sign</title>
<link rel="stylesheet" href="https://fonts.googleapis.com/css2?family=Open+Sans:ital,wght@0,300;0,400;0,700;1,300&display=swap">
<style>
  :root {
    --canvas: #ffffff;
    --sign-black: #000000;
    --sign-white: #ffffff;
    --divider: #6f6f6f;
  }
  html, body {
    margin: 0;
    padding: 0;
    width: 1200px;
    height: 1000px;
    overflow: hidden;
    background: var(--canvas);
  }
  .canvas {
    position: relative;
    width: 1200px;
    height: 1000px;
    font-family: "Open Sans", Arial, sans-serif;
    color: var(--sign-white);
  }
  .sign {
    position: absolute;
    left: 370px;
    top: 193px;
    width: 470px;
    height: 627px;
    background: var(--sign-black);
  }
  .sign-frame {
    position: absolute;
    left: 19px;
    top: 24px;
    width: 428px;
    height: 575px;
    border: 2px solid var(--sign-white);
    border-radius: 5px;
  }
  .headline {
    position: absolute;
    left: 0;
    top: 38px;
    width: 100%;
    margin: 0;
    text-align: center;
    font-weight: 700;
    font-size: 74px;
    line-height: 1;
    letter-spacing: 0.5px;
  }
  .divider {
    position: absolute;
    left: 32px;
    width: 406px;
    height: 1px;
    background: var(--divider);
  }
  .divider--top { top: 175px; }
  .divider--bottom { top: 432px; }
  .contact {
    position: absolute;
    left: 114px;
    top: 205px;
  }
  .agent-name {
    margin: 0;
    font-weight: 400;
    font-size: 26px;
    line-height: 1;
  }
  .phone {
    position: relative;
    margin: 20px 0 0;
    font-weight: 400;
    font-size: 48px;
    line-height: 1;
    letter-spacing: -0.5px;
  }
  .phone-icon {
    position: absolute;
    left: -46px;
    top: 14px;
    width: 36px;
    height: 26px;
  }
  .email {
    margin: 16px 0 0;
    font-weight: 300;
    font-style: italic;
    font-size: 16px;
    line-height: 1;
  }
  .website {
    margin: 38px 0 0;
    font-weight: 300;
    font-size: 22px;
    line-height: 1;
  }
  .brand {
    position: absolute;
    left: 0;
    top: 500px;
    width: 100%;
    display: flex;
    align-items: center;
    justify-content: center;
    gap: 14px;
  }
  .brand-mark {
    width: 22px;
    height: 22px;
    background: var(--sign-white);
  }
  .brand-name {
    font-weight: 700;
    font-size: 30px;
    line-height: 1;
  }
</style>
</head>
<body>
<div class="canvas">
  <div class="sign">
    <div class="sign-frame"></div>
    <h1 class="headline">FOR SALE</h1>
    <div class="divider divider--top"></div>
    <div class="contact">
      <p class="agent-name">Desmond Harlow</p>
      <p class="phone">
        <svg class="phone-icon" viewBox="0 0 36 26" aria-hidden="true">
          <g fill="none" stroke="#ffffff" stroke-width="1.6" stroke-linejoin="round">
            <path d="M4 22 L8 8 H30 L26 22 Z"/>
            <path d="M9 8 C10 3 12 2 15 2 H26 C29 2 30 4 30 8"/>
            <rect x="14" y="11" width="9" height="7"/>
          </g>
        </svg>
        0491 836 205
      </p>
      <p class="email">sales@brightlanerealestate.com.au</p>
      <p class="website">www.blrealestate.com.au</p>
    </div>
    <div class="divider divider--bottom"></div>
    <div class="brand">
      <span class="brand-mark"></span>
      <span class="brand-name">BrightLane Real Estate</span>
    </div>
  </div>
</div>
</body>
</html>
```